Parity Skills Forum needs a brochure to attract participants to its trainings

We need a flyer for our EU-funded project called " Parity Skills Forum" and it aims at increasing and developing skills of researchers and university staff members who are implementing measures towards gender equality in their institutions through our offered training programs. The final design should communicate gender equality for Research and Innovation centres and universities. This flyer will be distributed during conferences and events to our audience (mainly gender experts, researchers, administrative staff of universities, etc.) in order to provide the basic information about the project and options to get involved in the different trainings. We are attaching files to provide you with the concrete information on our requirements:- PS Forum flyer content.ppt: includes the content we would like to include in the flyer. There is also the URL to the project website and the different social media channels. - Project logo.zip: the project logo and guidelines as we would like to use colors that belong to the project logo color range. - Partners' logos.zip: Logos that will be included- EU flag: You can download different resolution files of the flag here: https://unionsymbols.example/about/flag_en -Regarding the images or graphics that you may include in the brochure we wouldn’t like to propose any because we do not want to limitate your imagination.

As it was not mentioned and we received a lot of questions about it, we prefer the flyer to be double-sided and in A5

Font styles to use
Serif
Sans Serif

Colors

Designer to choose colors to be used in the design.

Requirements
Nice to have
• At least 4 pages
Should not have
• We would not like to see as dominant colours the classic blue and pink.

```html
<!DOCTYPE html>
<html lang="en">
<head>
<meta charset="utf-8">
<title>Parity Skills Forum – Training Flyer</title>
<link rel="stylesheet" href="https://fonts.googleapis.com/css2?family=Roboto+Condensed:wght@400;700&family=Montserrat:wght@400;500;600;700&display=swap">
<style>
  :root{
    --magenta:#c4155a;
    --teal:#1bb4c6;
    --teal-dark:#129fb0;
    --ink:#1b1b1b;
    --body:#333333;
    --paper:#ffffff;
    --flag:#1f3d99;
  }
  *{box-sizing:border-box;margin:0;padding:0}
  html,body{width:708px;height:1200px;overflow:hidden;background:var(--paper)}
  body{font-family:"Montserrat",Arial,sans-serif;color:var(--body);position:relative}

  .hero-photo{position:absolute;left:0;top:0;width:708px;height:600px;
    background:
      radial-gradient(ellipse 260px 200px at 330px 330px,#e9e4dc 0%,rgba(233,228,220,0) 70%),
      radial-gradient(ellipse 200px 240px at 90px 200px,#c9b79a 0%,rgba(201,183,154,0) 75%),
      radial-gradient(ellipse 240px 180px at 560px 120px,#7c8f5f 0%,rgba(124,143,95,0) 75%),
      linear-gradient(180deg,#8d9474 0%,#9a8f80 35%,#6f6a6a 65%,#4f4b55 100%);}
  .hero-wave{position:absolute;left:0;top:500px;width:708px;height:110px}

  .brand{position:absolute;right:40px;top:40px;display:flex;align-items:center;gap:12px}
  .brand-mark{width:48px;height:48px;background:var(--magenta)}
  .brand-name{font-family:"Montserrat",Arial,sans-serif;font-weight:500;font-size:27px;color:var(--ink);letter-spacing:.5px}

  .funding{position:absolute;left:30px;top:600px;width:330px;display:flex;gap:10px;align-items:center}
  .funder-flag{width:40px;height:27px;background:var(--flag);flex:none}
  .funding p{font-size:7.5px;line-height:1.35;color:#444}

  .headline{position:absolute;left:30px;top:640px;width:340px;font-family:"Roboto Condensed",Arial,sans-serif;font-weight:700;font-size:24px;line-height:27px;color:var(--magenta)}
  .headline .accent{color:var(--teal)}
  .headline .scope{font-weight:400}
  .formats{position:absolute;left:30px;top:758px;width:340px;font-family:"Montserrat",Arial,sans-serif;font-weight:700;font-size:14.5px;line-height:19px;color:var(--ink)}

  .section-title{font-family:"Roboto Condensed",Arial,sans-serif;font-weight:700;font-size:22px;color:var(--magenta);display:inline-block;padding-bottom:3px;border-bottom:2px solid var(--teal);margin-bottom:12px}

  .col{position:absolute}
  .col-left{left:30px;top:832px;width:330px}
  .col-right{left:385px;top:604px;width:300px}

  .ticks{list-style:none}
  .ticks li{position:relative;padding-left:18px;font-size:10.5px;line-height:1.4;margin-bottom:10px;color:var(--body)}
  .ticks li::before{content:"";position:absolute;left:0;top:3px;width:8px;height:8px;border:1.5px solid var(--teal)}
  .ticks li::after{content:"";position:absolute;left:3px;top:4px;width:3px;height:5px;border:solid var(--magenta);border-width:0 1.5px 1.5px 0;transform:rotate(45deg)}
  .col-right .ticks{margin-left:10px}

  .need{margin:2px 0 8px 20px;font-size:8.5px;line-height:1.35}
  .need b{color:var(--magenta);font-weight:600}
  .summary{font-size:8.5px;line-height:1.35;font-style:italic;font-weight:600;color:var(--ink);margin-bottom:14px}

  .contact-bar{position:absolute;left:0;top:1094px;width:708px;height:50px;background:var(--teal);display:flex;align-items:center;justify-content:space-between;padding:0 30px}
  .contact-bar .ask{color:#fff}
  .contact-bar .ask strong{display:block;font-family:"Roboto Condensed",Arial,sans-serif;font-size:15px;font-weight:700}
  .contact-bar .ask span{font-size:9.5px}
  .channels{width:300px;color:#fff;font-family:"Roboto Condensed",Arial,sans-serif;font-weight:700;font-size:16px;line-height:20px}
  .channels div{display:flex;align-items:center;gap:10px}
  .channels svg{width:13px;height:13px;flex:none}

  .partners{position:absolute;left:0;top:1144px;width:708px;height:56px;display:flex;align-items:center;justify-content:space-between;padding:0 26px}
  .partner{height:16px;background:#c9cfd4;border-radius:2px}
  .partner.round{width:18px;height:18px;border-radius:50%}
</style>
</head>
<body>

<div class="hero-photo" role="img" aria-label="Photo: hands holding a card showing the male and female symbols joined by an equals sign, blurred city crowd behind"></div>

<svg class="hero-wave" viewBox="0 0 708 110" preserveAspectRatio="none" aria-hidden="true">
  <path d="M0 62 C180 20 420 30 708 0 L708 110 L0 110 Z" fill="var(--teal)"/>
  <path d="M0 72 C180 32 420 44 708 14 L708 110 L0 110 Z" fill="var(--paper)"/>
</svg>

<div class="brand">
  <span class="brand-mark"></span>
  <span class="brand-name">PS Forum</span>
</div>

<div class="funding">
  <span class="funder-flag" role="img" aria-label="Funding programme flag"></span>
  <p>This project has received funding from the Civic Research Fund's research and innovation programme under grant agreement No 000000.</p>
</div>

<h1 class="headline">A high-quality capacity-building programme on <span class="accent">GENDER EQUALITY</span><br><span class="scope">IN RESEARCH, INNOVATION AND HIGHER EDUCATION</span></h1>

<p class="formats">In person-trainings | Workshops |<br>Summer Schools | DOCCs | Webinars |<br>Train-the-Trainers sessions</p>

<section class="col col-left">
  <h2 class="section-title">Training Offers</h2>
  <ul class="ticks">
    <li>Trainings are offered for free to those interested to understand and consider gender equality and dimension as an integral part of research and innovation.</li>
    <li>Find the offer which suits you best and register on https://psforum.example/</li>
    <li>There are different dates and locations</li>
    <li>Course Language: English</li>
    <li>Participation is free thanks to the CRF.</li>
  </ul>
</section>

<section class="col col-right">
  <h2 class="section-title">The challenge</h2>
  <ul class="ticks">
    <li>Currently, there are many programmes, projects and a great gained knowledge and experience, <b>BUT</b> :</li>
    <li>Gender analysis remains rarely appropriated within research projects</li>
    <li>Large differences among research performing organisations in various countries</li>
    <li>Small proportion of researchers and practitioners are familiar with theoretical and methodological concepts of gender and feminist scholarship</li>
  </ul>
  <p class="need"><b>Need:</b> A holistic approach to structural change for gender equality in R&amp;I</p>
  <p class="summary">The Parity Skills Forum project offers high-quality capacity-building programme on gender equality in research, innovation and higher education</p>

  <h2 class="section-title">Get Involved</h2>
  <ul class="ticks">
    <li>Take part in one or more offered trainings</li>
    <li>Become a gender trainer</li>
    <li>Become a host institution to the topic of your preference</li>
    <li>Be part of the pan European gender trainers' network</li>
  </ul>
</section>

<footer class="contact-bar">
  <div class="ask">
    <strong>Do you still have questions? Feel free to contact us</strong>
    <span>A member of the team will make her/his best to reply as soon as possible</span>
  </div>
  <div class="channels">
    <div><svg viewBox="0 0 14 14" aria-hidden="true"><rect x="1" y="3" width="12" height="8" fill="none" stroke="var(--magenta)" stroke-width="1.6"/><path d="M1 3 L7 8 L13 3" fill="none" stroke="var(--magenta)" stroke-width="1.6"/></svg>info@psforum.example</div>
    <div><svg viewBox="0 0 14 14" aria-hidden="true"><circle cx="7" cy="7" r="5.5" fill="none" stroke="var(--magenta)" stroke-width="1.6"/><path d="M1.5 7 H12.5 M7 1.5 C4 5 4 9 7 12.5 M7 1.5 C10 5 10 9 7 12.5" fill="none" stroke="var(--magenta)" stroke-width="1.2"/></svg>https://psforum.example/</div>
  </div>
</footer>

<div class="partners" aria-label="Project partners">
  <span class="partner" style="width:46px"></span>
  <span class="partner" style="width:40px"></span>
  <span class="partner" style="width:44px"></span>
  <span class="partner" style="width:52px"></span>
  <span class="partner" style="width:34px"></span>
  <span class="partner round"></span>
  <span class="partner" style="width:30px"></span>
  <span class="partner" style="width:26px"></span>
  <span class="partner round"></span>
  <span class="partner" style="width:24px"></span>
  <span class="partner" style="width:42px"></span>
</div>

</body>
</html>
```